Powerpoint template for Waste Management company

We need a professional look and feeling for our powerpoint presentation templates. Company is based on three pillars: componsting solutions, collecting solutions and recycling solutions. We area looking for ppt templates for the front page, regular slide and at leat one slide template specific for each pillar (total 5-6 slide templates). I have attached the logo.

Target Market(s)

Companies, Goverment, Municipalities

Industry/Entity Type

Waste Management

Font styles to use
Serif

```html
<!DOCTYPE html>
<html lang="en">
<head>
<meta charset="utf-8">
<title>Greenrow Waste Services – Presentation Templates</title>
<link href="https://fonts.googleapis.com/css2?family=Varela+Round&family=Raleway:wght@400;500;600&display=swap" rel="stylesheet">
<style>
:root{
  --green:#3bb54a;
  --orange:#f15a24;
  --blue:#0071bc;
  --grey:#6d6b6b;
  --truck:#7a7a7a;
  --text:#8a8a8a;
  --logo-bg:#efefef;
  --page:#ffffff;
}
*{box-sizing:border-box;margin:0;padding:0}
html,body{width:1059px;height:1200px;overflow:hidden;background:var(--page)}
body{position:relative;font-family:"Raleway",sans-serif;color:var(--text)}
.slide{position:absolute;width:514px;height:290px;background:#fff;overflow:hidden;box-shadow:0 1px 4px rgba(0,0,0,.28)}
.col-l{left:7px}.col-r{left:537px}
.row1{top:5px}.row2{top:304px}.row3{top:603px}.row4{top:902px}
.abs{position:absolute}

/* brand mark */
.brand{position:absolute;background:var(--logo-bg);border-top:3px solid var(--green);border-bottom:3px solid var(--green);display:flex;align-items:center;gap:5px;padding:0 8px}
.brand-dot{width:9px;height:9px;background:var(--green);flex:none}
.brand-name{font-family:"Varela Round",sans-serif;color:#555;font-size:7px;line-height:1.05}
.brand.sm{width:51px;height:25px;top:11px;right:10px;padding:0 4px;gap:3px;border-width:2px}
.brand.sm .brand-dot{width:5px;height:5px}
.brand.sm .brand-name{font-size:4px}

/* cover / section */
.band{position:absolute;left:0;right:0}
.accent{position:absolute;left:0;width:22px}
.hero-title{position:absolute;left:27px;font-family:"Varela Round",sans-serif;font-size:35px;line-height:33px;font-weight:400;-webkit-text-stroke:.6px currentColor}
.hero-sub{position:absolute;left:27px;font-size:9px;font-weight:500}
.legal{position:absolute;right:28px;font-size:6px;font-weight:600}

/* content slides */
.head{position:absolute;left:0;right:0;top:0;height:47px;border-bottom:3px solid}
.head h2{position:absolute;left:28px;top:14px;color:#fff;font-family:"Varela Round",sans-serif;font-size:20px;font-weight:400;-webkit-text-stroke:.3px #fff}
.foot{position:absolute;left:6px;bottom:7px;font-size:5.5px;color:var(--green)}
.pagenum{position:absolute;right:14px;bottom:6px;font-size:6px;color:var(--blue)}
.placeholder{position:absolute;border-radius:6px}

.stat-label{position:absolute;font-size:9px;color:#777}
.stat-num{position:absolute;font-family:"Varela Round",sans-serif;font-size:26px;-webkit-text-stroke:.6px currentColor}
.stat-desc{position:absolute;font-size:5.5px;line-height:1.3;width:100px;text-align:justify}
.rule{position:absolute;left:135px;width:178px;border-top:1px dotted #aaa}
.rule::after{content:"";position:absolute;right:-2px;top:-2.5px;width:3px;height:3px;border-radius:50%;background:#999}
.chart-note{position:absolute;left:331px;top:192px;width:152px;font-size:5.3px;line-height:1.9;text-align:justify}

.truck-label{position:absolute;font-size:9px;color:#777}
.truck-value{position:absolute;font-family:"Raleway",sans-serif;font-size:22px;font-weight:500}
.truck-desc{position:absolute;width:110px;font-size:6.6px;line-height:2;text-align:justify;word-spacing:2px}

.step{position:absolute;left:44px;width:147px}
.step-tag{height:12px;color:#fff;font-size:7.5px;padding:1px 3px}
.step ul{list-style:none;margin-top:3px}
.step li{font-size:6.4px;line-height:13px;padding-left:13px;position:relative}
.step li::before{content:"•";position:absolute;left:3px}

.thanks{position:absolute;left:33px;top:108px;font-family:"Varela Round",sans-serif;font-size:44px;line-height:50px;color:var(--grey);-webkit-text-stroke:1px var(--grey)}
</style>
</head>
<body>

<!-- 1 cover -->
<section class="slide col-l row1">
  <div class="brand" style="left:30px;top:12px;width:87px;height:50px"><span class="brand-dot"></span><span class="brand-name">Greenrow<br>Waste Services</span></div>
  <div class="band" style="top:71px;height:167px;background:var(--green)"></div>
  <div class="accent" style="top:109px;height:91px;background:var(--blue)"></div>
  <h1 class="hero-title" style="top:112px;color:#fff">Business<br>Presentation</h1>
  <p class="hero-sub" style="top:187px;color:#fff">Your Subtitle Goes Here</p>
  <p class="legal" style="top:261px;color:var(--green)">© 2017 Greenrow Waste Services. All rights reserved.</p>
</section>

<!-- 2 composting section -->
<section class="slide col-r row1">
  <div class="band" style="top:0;height:71px;background:var(--green)"></div>
  <div class="brand" style="left:30px;top:15px;width:87px;height:43px;border:none"><span class="brand-dot"></span><span class="brand-name">Greenrow<br>Waste Services</span></div>
  <div class="accent" style="top:109px;height:91px;background:var(--green)"></div>
  <h1 class="hero-title" style="top:112px;color:var(--grey)">Componsting<br>Solutions</h1>
  <p class="hero-sub" style="top:187px;color:var(--grey)">Your Subtitle Goes Here</p>
  <div class="band" style="top:238px;height:52px;background:var(--green)"></div>
  <p class="legal" style="top:261px;color:#fff">© 2017 Greenrow Waste Services. All rights reserved.</p>
</section>

<!-- 3 composting content -->
<section class="slide col-l row2">
  <div class="head" style="background:var(--green);border-color:var(--orange)"><h2>Componsting Solutions</h2></div>
  <div class="brand sm"><span class="brand-dot"></span><span class="brand-name">Greenrow<br>Waste Services</span></div>
  <div class="placeholder" role="img" aria-label="Leaf illustration divided into blue, orange and green sections" style="left:34px;top:70px;width:100px;height:196px;background:linear-gradient(170deg,var(--blue),var(--orange) 50%,var(--green))"></div>
  <div class="rule" style="top:69px"></div>
  <div class="rule" style="top:144px;left:145px;width:168px"></div>
  <div class="rule" style="top:200px;left:145px;width:168px"></div>
  <p class="stat-label" style="left:135px;top:79px">Insert Text</p>
  <p class="stat-num" style="left:135px;top:91px;color:var(--blue)">43%</p>
  <p class="stat-desc" style="left:196px;top:98px">All files and graphics on this template is editable because is all based on vector</p>
  <p class="stat-label" style="left:143px;top:146px">Insert Text</p>
  <p class="stat-num" style="left:143px;top:157px;color:var(--green)">32%</p>
  <p class="stat-desc" style="left:204px;top:164px">All files and graphics on this template is editable because is all based on vector</p>
  <p class="stat-label" style="left:137px;top:208px">Insert Text</p>
  <p class="stat-num" style="left:137px;top:220px;color:var(--green)">27%</p>
  <p class="stat-desc" style="left:198px;top:227px">All files and graphics on this template is editable because is all based on vector</p>
  <svg class="abs" style="left:325px;top:85px" width="160" height="105" viewBox="0 0 160 105">
    <g font-family="Raleway,sans-serif" font-size="5" fill="#777" text-anchor="end">
      <text x="10" y="5">3</text><text x="10" y="19">2,5</text><text x="10" y="33">2</text>
      <text x="10" y="47">1,5</text><text x="10" y="60">1</text><text x="10" y="74">0,5</text><text x="10" y="88">0</text>
    </g>
    <line x1="15" y1="87" x2="150" y2="87" stroke="#ccc" stroke-width=".6"/>
    <rect x="48" y="33" width="22" height="54" fill="#3bb54a"/>
    <rect x="71" y="21" width="22" height="66" fill="#f15a24"/>
    <rect x="94" y="11" width="22" height="76" fill="#0071bc"/>
    <text x="82" y="99" font-family="Raleway,sans-serif" font-size="5" fill="#666" text-anchor="middle">Category 1</text>
  </svg>
  <p class="chart-note">For every 6 emails received, we get 3 Phone calls. Suitable for all categories business and personal presentation, Suitable for all categories business and personal presentation, eaque ipsa quae ab illo inventore veritatis et quasi</p>
  <p class="foot">© 2017 Greenrow Waste Services. All rights reserved</p>
  <p class="pagenum">3</p>
</section>

<!-- 4 collecting section -->
<section class="slide col-r row2">
  <div class="band" style="top:0;height:71px;background:var(--orange)"></div>
  <div class="brand" style="left:30px;top:12px;width:87px;height:50px"><span class="brand-dot"></span><span class="brand-name">Greenrow<br>Waste Services</span></div>
  <div class="accent" style="top:109px;height:91px;background:var(--orange)"></div>
  <h1 class="hero-title" style="top:112px;color:var(--grey)">Collecting<br>Solutions</h1>
  <p class="hero-sub" style="top:187px;color:var(--grey)">Your Subtitle Goes Here</p>
  <div class="band" style="top:238px;height:52px;background:var(--orange)"></div>
  <p class="legal" style="top:261px;color:#fff">© 2017 Greenrow Waste Services. All rights reserved.</p>
</section>

<!-- 5 collecting content -->
<section class="slide col-l row3">
  <div class="head" style="background:var(--orange);border-color:var(--blue)"><h2>Collecting Solutions</h2></div>
  <div class="brand sm"><span class="brand-dot"></span><span class="brand-name">Greenrow<br>Waste Services</span></div>
  <div class="placeholder" role="img" aria-label="Grey dump truck carrying an orange load" style="left:24px;top:92px;width:121px;height:78px;background:linear-gradient(180deg,var(--orange),var(--truck) 55%)"></div>
  <div class="placeholder" role="img" aria-label="Grey dump truck carrying a green load" style="left:190px;top:88px;width:121px;height:82px;background:linear-gradient(180deg,var(--green),var(--truck) 55%)"></div>
  <div class="placeholder" role="img" aria-label="Grey dump truck carrying a blue load" style="left:357px;top:91px;width:121px;height:79px;background:linear-gradient(180deg,var(--blue),var(--truck) 55%)"></div>
  <p class="truck-label" style="left:31px;top:180px">Waste</p>
  <p class="truck-value" style="left:29px;top:192px;color:var(--orange)">$2M</p>
  <p class="truck-desc" style="left:29px;top:222px">Click the shape on truck, ungroup it and recolor a fill with your own.</p>
  <p class="truck-label" style="left:196px;top:180px">waste</p>
  <p class="truck-value" style="left:194px;top:192px;color:var(--green)">$5M</p>
  <p class="truck-desc" style="left:194px;top:222px">Click the shape on truck, ungroup it and recolor a fill with your own.</p>
  <p class="truck-label" style="left:362px;top:180px">waste</p>
  <p class="truck-value" style="left:361px;top:192px;color:var(--blue)">$3,5M</p>
  <p class="truck-desc" style="left:361px;top:222px">Click the shape on truck, ungroup it and recolor a fill with your own.</p>
  <p class="foot">© 2017 Greenrow Waste Services. All rights reserved</p>
  <p class="pagenum">5</p>
</section>

<!-- 6 recycling section -->
<section class="slide col-r row3">
  <div class="band" style="top:0;height:71px;background:var(--blue)"></div>
  <div class="brand" style="left:30px;top:12px;width:87px;height:50px"><span class="brand-dot"></span><span class="brand-name">Greenrow<br>Waste Services</span></div>
  <div class="accent" style="top:109px;height:91px;background:var(--blue)"></div>
  <h1 class="hero-title" style="top:112px;color:var(--grey)">Recycling<br>Solutions</h1>
  <p class="hero-sub" style="top:187px;color:var(--grey)">Your Subtitle Goes Here</p>
  <div class="band" style="top:238px;height:52px;background:var(--blue)"></div>
  <p class="legal" style="top:261px;color:#fff">© 2017 Greenrow Waste Services. All rights reserved.</p>
</section>

<!-- 7 recycling content -->
<section class="slide col-l row4">
  <div class="head" style="background:var(--blue);border-color:var(--green)"><h2>Recycling Solutions</h2></div>
  <div class="brand sm"><span class="brand-dot"></span><span class="brand-name">Greenrow<br>Waste Services</span></div>
  <div class="step" style="top:81px">
    <div class="step-tag" style="background:var(--blue)">Input</div>
    <ul style="color:#777"><li>Donec eu dui eget nisl rhoncus volutpat.</li><li>Quisque et magna faucibus vestibulum.</li><li>Donec convallis mauris rutrum finibus.</li></ul>
  </div>
  <div class="step" style="top:148px">
    <div class="step-tag" style="background:var(--orange)">Process</div>
    <ul style="color:#777"><li>Donec eu dui eget nisl rhoncus volutpat.</li><li>Quisque et magna faucibus vestibulum.</li></ul>
  </div>
  <div class="step" style="top:202px">
    <div class="step-tag" style="background:var(--green)">Output</div>
    <ul style="color:#777"><li>Donec eu dui eget nisl rhoncus volutpat.</li><li>Quisque et magna faucibus vestibulum.</li><li>Donec convallis mauris rutrum finibus.</li></ul>
  </div>
  <div class="placeholder" role="img" aria-label="Recycling cycle illustration with input, process and output arrows" style="left:272px;top:83px;width:196px;height:178px;background:linear-gradient(135deg,var(--blue),var(--orange) 50%,var(--green))"></div>
  <p class="foot">© 2017 Greenrow Waste Services. All rights reserved</p>
  <p class="pagenum">7</p>
</section>

<!-- 8 closing -->
<section class="slide col-r row4">
  <div class="band" style="top:0;height:71px;background:var(--blue)"></div>
  <div class="accent" style="top:112px;height:90px;background:var(--blue)"></div>
  <h1 class="thanks">Thank<br>You</h1>
  <div class="brand" style="left:340px;top:113px;width:145px;height:83px;border-width:5px;gap:7px;padding:0 14px"><span class="brand-dot" style="width:13px;height:13px"></span><span class="brand-name" style="font-size:11px">Greenrow<br>Waste Services</span></div>
  <div class="band" style="top:237px;height:53px;background:var(--blue)"></div>
</section>

</body>
</html>
```